Golden Ladle Club April Competition

The website slider is 990 X 225 pixels to fit in with this website www.goldenladleclub.com.au

We would love a fun, lively, food-oriented slider created for Golden Ladle Club website. Golden Ladle Club is a central place where people who love food, cooking for their family and friends, and sharing recipes can hang out. We'd like the sliders to be simple, bright and to entice people to click on the link.

The banner ad needs to feature the Southern Hearth Monthly cookbooks, and to use a colour scheme that also works with the existing website.

A slider in March was used to promote a similar competition which I will upload as inspiration, along with the image of the cook books to use.

Main text: Add your best mid-week meal recipes to win one of 8 cookbook sets!
Smaller text: The 8 best recipes as chosen by Golden Ladle Club editors will win.

```html
<!DOCTYPE html>
<html lang="en">
<head>
<meta charset="utf-8">
<title>Golden Ladle Club – April Competition Slider</title>
<link rel="stylesheet" href="https://fonts.googleapis.com/css2?family=Nunito:ital,wght@1,800&family=Oswald:wght@600&display=swap">
<style>
  :root {
    --stage-bg-light: #6a6a6a;
    --stage-bg-dark: #474747;
    --panel-dark: #0b2427;
    --panel-mid: #1d4a4e;
    --panel-edge: #1f7a5a;
    --photo-light: #f7f8f8;
    --photo-shade: #e3e8ea;
    --text-white: #ffffff;
    --text-accent: #45d3dc;
    --headline-top: #4fe6c4;
    --headline-bottom: #12a48f;
    --text-muted: #c9d1d2;
  }
  html, body {
    margin: 0;
    padding: 0;
    width: 1200px;
    height: 433px;
    overflow: hidden;
  }
  body {
    background: radial-gradient(ellipse 70% 80% at 50% 30%, var(--stage-bg-light), var(--stage-bg-dark));
    position: relative;
  }
  .slider {
    position: absolute;
    left: 77px;
    top: 73px;
    width: 1046px;
    height: 241px;
    box-shadow: 0 4px 10px rgba(0, 0, 0, 0.35);
  }
  .slider__photo {
    position: absolute;
    left: 0;
    top: 0;
    width: 360px;
    height: 241px;
    background: linear-gradient(160deg, var(--photo-light) 0%, var(--photo-shade) 100%);
  }
  .slider__panel {
    position: absolute;
    inset: 0;
    width: 1046px;
    height: 241px;
  }
  .slider__copy {
    position: absolute;
    right: 42px;
    top: 0;
    width: 640px;
    text-align: right;
  }
  .slider__lead {
    position: absolute;
    right: 0;
    top: 48px;
    margin: 0;
    font-family: "Nunito", Arial, sans-serif;
    font-style: italic;
    font-weight: 800;
    font-size: 25px;
    color: var(--text-white);
    white-space: nowrap;
    text-shadow: 0 1px 2px rgba(0, 0, 0, 0.6);
  }
  .slider__lead-accent {
    color: var(--text-accent);
  }
  .slider__headline {
    position: absolute;
    right: 0;
    top: 86px;
    margin: 0;
    font-family: "Oswald", Impact, sans-serif;
    font-weight: 600;
    font-size: 42px;
    line-height: 1;
    letter-spacing: 0.5px;
    white-space: nowrap;
    background: linear-gradient(180deg, var(--headline-top), var(--headline-bottom));
    -webkit-background-clip: text;
    background-clip: text;
    color: transparent;
    filter: drop-shadow(0 2px 2px rgba(0, 0, 0, 0.6));
  }
  .slider__note {
    position: absolute;
    right: 0;
    top: 146px;
    margin: 0;
    font-family: "Nunito", Arial, sans-serif;
    font-style: italic;
    font-weight: 800;
    font-size: 15px;
    color: var(--text-muted);
    white-space: nowrap;
  }
</style>
</head>
<body>
  <section class="slider" aria-label="April competition slider">
    <div class="slider__photo" role="img" aria-label="Three Southern Hearth Monthly cookbooks – salad, pizza and cooking class titles – fanned on a white background"></div>

    <svg class="slider__panel" viewBox="0 0 1046 241" aria-hidden="true">
      <defs>
        <radialGradient id="panelGlow" cx="0.6" cy="0.45" r="0.65">
          <stop offset="0" stop-color="var(--panel-mid)"/>
          <stop offset="1" stop-color="var(--panel-dark)"/>
        </radialGradient>
      </defs>
      <polygon points="342,0 1046,0 1046,241 293,241" fill="url(#panelGlow)"/>
      <line x1="342" y1="1.5" x2="1046" y2="1.5" stroke="var(--panel-edge)" stroke-width="3"/>
      <line x1="293" y1="239.5" x2="1046" y2="239.5" stroke="var(--panel-edge)" stroke-width="3"/>
    </svg>

    <div class="slider__copy">
      <p class="slider__lead">Add your best&nbsp; <span class="slider__lead-accent">mid-week meal recipes</span> to</p>
      <h1 class="slider__headline">WIN ONE OF 8 COOKBOOK SETS!</h1>
      <p class="slider__note">The 8 best recipes as chosen by Golden Ladle Club editors will win.</p>
    </div>
  </section>
</body>
</html>
```